Retail Jewelry Business Card Design Project

We are in need of a new business card design for a retail jewelry store. This store is in the business of fine jewelry including but not specific to bridal jewelry, diamonds, designer jewelry and watches.

This store has been in business for 20 years but continues to strive for a modern professional appeal. The main colors use for this business are a royal blue, white and silver.

Target Market(s)

Target market is ages 18-50

Industry/Entity Type

Jewelry

Requirements
Must have
• Sales Person Name
Sales Person Email Address

Store Address
Store Phone
Website

Standard business card size. No odd shapes or sizes.
Nice to have
• Overall modern feel for card.

We have thought that a design with a nice feature of the logo on the back of the card would be nice but open to ideas.
Should not have
• No specific images of jewelry should be used.

```html
<!DOCTYPE html>
<html lang="en">
<head>
<meta charset="utf-8">
<title>Marlowe Reed Fine Jewelry – Business Cards</title>
<link rel="stylesheet" href="https://fonts.googleapis.com/css2?family=Cinzel:wght@400;600&display=swap">
<style>
  :root {
    --backdrop: #2b1811;
    --royal: #2e2e96;
    --royal-light: #3a3ab2;
    --paper: #ffffff;
    --silver: #e6e6f0;
    --ink: #2f2f9a;
  }
  * { margin: 0; padding: 0; box-sizing: border-box; }
  html, body { width: 1200px; height: 1000px; overflow: hidden; }
  body {
    background: var(--backdrop);
    font-family: "Cinzel", Georgia, serif;
    position: relative;
  }
  .card {
    position: absolute;
    overflow: hidden;
    box-shadow: 0 8px 24px rgba(0,0,0,0.55);
    text-align: center;
  }
  .card-front { left: 160px; top: 85px; width: 380px; height: 620px; background: var(--paper); }
  .card-back {
    left: 655px; top: 335px; width: 360px; height: 600px;
    background: linear-gradient(160deg, var(--royal-light), var(--royal) 60%);
  }
  .brand {
    position: absolute; left: 0; right: 0;
    font-weight: 400; line-height: 1.15;
  }
  .brand-name { display: block; font-size: 38px; }
  .brand-sub { display: block; font-size: 19px; letter-spacing: 2px; }
  .card-front .brand { top: 92px; color: var(--ink); }
  .card-back .brand { top: 48px; color: var(--silver); }
  .person { position: absolute; left: 0; right: 0; top: 262px; color: var(--ink); }
  .person-name { font-size: 21px; }
  .person-email { font-size: 13.5px; margin-top: 6px; letter-spacing: 0.3px; text-transform: lowercase; font-variant: small-caps; }
  .store-band {
    position: absolute; left: 0; right: 0; bottom: 0; height: 200px;
    background: linear-gradient(160deg, var(--royal-light), var(--royal) 70%);
    color: var(--paper);
    padding-top: 42px;
    font-size: 17px; line-height: 25px;
  }
  .store-band .web { letter-spacing: 0.6px; }
  .mark-spot { position: absolute; left: 105px; top: 215px; }
  .back-web {
    position: absolute; left: 0; right: 0; top: 518px;
    color: var(--silver); font-size: 15.5px; letter-spacing: 0.6px;
  }
</style>
</head>
<body>
  <section class="card card-front">
    <div class="brand">
      <span class="brand-name">Marlowe Reed</span>
      <span class="brand-sub">FINE JEWELRY</span>
    </div>
    <div class="person">
      <div class="person-name">Marlowe Reed Hastings</div>
      <div class="person-email">marlowe@marlowereedjewelry.com</div>
    </div>
    <div class="store-band">
      <div>Marlowe Reed Fine</div>
      <div>2281 Larkspur Avenue</div>
      <div>Bayview, FL 32099</div>
      <div class="web">www.marlowereedjewelry.com</div>
    </div>
  </section>

  <section class="card card-back">
    <div class="brand">
      <span class="brand-name">Marlowe Reed</span>
      <span class="brand-sub">FINE JEWELRY</span>
    </div>
    <svg class="mark-spot" width="150" height="150" viewBox="0 0 150 150" aria-hidden="true">
      <circle cx="75" cy="75" r="70" fill="none" stroke="#e6e6f0" stroke-width="3"/>
    </svg>
    <div class="back-web">www.marlowereedjewelry.com</div>
  </section>
</body>
</html>
```